Web Design Project

We are re-starting this project.

This project is for a totally new look and design of a website for Wablor. www.wablor-demo.net.

Wablor is a naming protocol for physical locations and can be used for fixed and mobile people, places and things. Find your friends, or find a business. Because Wablor locations point to precise geo-physical (GPS) co-ordinates, navigation to a location becomes totally reliable.
Updates

Please see the modified brief for this project

Target Market(s)

Every person and every business can have multiple !Wabs (Wablor locations), so the website needs to be appealing and fun, but easy to use and functional

Industry/Entity Type

Business

Colors
34a6d7

Requirements
Must have
• Uniqueness!

```html
<!DOCTYPE html>
<html lang="en">
<head>
<meta charset="utf-8">
<title>Wablor – Social Positioning</title>
<link rel="stylesheet" href="https://fonts.googleapis.com/css2?family=Ubuntu:ital,wght@0,400;0,500;0,700;1,400&display=swap">
<style>
  :root {
    --brand: #34a6d7;
    --brand-dark: #2a8fbc;
    --ink: #3a3a3a;
    --ink-soft: #555b60;
    --header-bg: #edf1f4;
    --footer-bg: rgba(236, 239, 242, 0.94);
    --card-bg: #f3f3f3;
    --white: #ffffff;
  }
  * { box-sizing: border-box; margin: 0; padding: 0; }
  html, body { width: 1200px; height: 669px; overflow: hidden; }
  body {
    font-family: "Ubuntu", sans-serif;
    color: var(--ink);
    background: var(--white);
    position: relative;
  }

  /* Header */
  .site-header {
    position: absolute; left: 0; top: 0; width: 1200px; height: 84px;
    background: linear-gradient(#f4f6f8, var(--header-bg));
  }
  .brand {
    position: absolute; left: 171px; top: 18px;
    display: flex; align-items: center; gap: 8px;
    font-size: 40px; font-weight: 700; color: var(--brand);
    letter-spacing: -0.5px; text-decoration: none;
  }
  .brand-dot { width: 28px; height: 28px; border-radius: 50%; background: var(--brand); }
  .account-nav {
    position: absolute; right: 171px; top: 37px;
    display: flex; gap: 12px; font-size: 14px; font-weight: 500;
  }
  .account-nav a { color: var(--brand); text-decoration: none; display: flex; align-items: center; gap: 5px; }
  .account-nav svg { width: 12px; height: 12px; }

  /* Hero */
  .hero-scene {
    position: absolute; left: 0; top: 84px; width: 1200px; height: 539px;
    background:
      radial-gradient(ellipse 260px 300px at 260px 300px, rgba(40,40,42,0.85), rgba(40,40,42,0) 70%),
      linear-gradient(180deg, #b9c3cb 0%, #a7adb0 35%, #b49d85 70%, #c8b39d 100%);
  }

  .finder-marker {
    position: absolute; left: 816px; top: 170px;
    width: 40px; height: 40px; border-radius: 50%; background: var(--brand);
  }
  .finder {
    position: absolute; left: 689px; top: 228px; width: 293px; height: 102px;
    border: 1px solid var(--brand); border-radius: 4px;
    background: rgba(255,255,255,0.55); padding: 4px;
  }
  .finder-inner {
    background: var(--card-bg); border-radius: 3px; height: 100%;
    padding: 14px 12px 0;
  }
  .finder-title { font-size: 19.5px; font-weight: 500; color: var(--ink); }
  .finder-input {
    display: block; margin-top: 11px; width: 263px; height: 25px;
    border: 1px solid #c6c6c6; border-radius: 3px; background: var(--white);
    font: italic 14px "Ubuntu", sans-serif; color: #555; padding: 0 9px;
  }
  .finder-button {
    position: absolute; left: 771px; top: 330px; width: 129px; height: 31px;
    background: var(--brand); color: var(--white); border: 0;
    font: 500 18px "Ubuntu", sans-serif;
  }

  .activity {
    position: absolute; left: 643px; top: 403px; width: 386px; height: 99px;
    background: var(--card-bg); border-radius: 4px; overflow: hidden;
  }
  .activity-title {
    height: 25px; background: var(--brand); color: var(--white);
    font-size: 12px; font-weight: 500; text-align: center; line-height: 25px;
  }
  .activity-list { list-style: none; padding: 0 8px; }
  .activity-item {
    font-size: 11px; color: var(--ink-soft); text-align: center;
    height: 26px; line-height: 26px;
  }
  .activity-item + .activity-item { border-top: 1px solid #dcdcdc; }
  .activity-time { color: var(--brand); font-weight: 500; }
  .activity-more {
    position: absolute; left: 815px; top: 502px; width: 42px; height: 16px;
    background: var(--brand); display: flex; align-items: center; justify-content: center;
  }

  .support-tab {
    position: absolute; left: 853px; top: 592px; width: 175px; height: 31px;
    background: var(--white); border: 2px solid var(--brand); border-bottom: 0;
    border-radius: 4px 4px 0 0; font-size: 16px; font-weight: 500; color: var(--ink);
    text-align: center; line-height: 29px;
  }

  /* Footer */
  .site-footer {
    position: absolute; left: 0; top: 623px; width: 1200px; height: 46px;
    background: var(--footer-bg);
    font-size: 12.5px; font-weight: 500; color: var(--ink);
  }
  .footer-nav { position: absolute; left: 173px; top: 16px; display: flex; }
  .footer-nav a { color: var(--ink); text-decoration: none; }
  .footer-nav a + a::before { content: "|"; margin: 0 7px; color: var(--ink); }
  .powered-by { position: absolute; right: 171px; top: 16px; }
</style>
</head>
<body>
  <header class="site-header">
    <a class="brand" href="#"><span class="brand-dot"></span>Wablor</a>
    <nav class="account-nav">
      <a href="#"><svg viewBox="0 0 12 12"><path d="M2 1h5l-1 1H2.5v8.5h7V6l1-1v6H1.5V1z M10 1l1.3 1.3L6 7.6 4.5 8l.4-1.5z" fill="#444"/></svg>Sign Up</a>
      <a href="#"><svg viewBox="0 0 12 12"><circle cx="6" cy="3.5" r="2.7" fill="#444"/><path d="M0.8 12c0-3.3 2.3-5 5.2-5s5.2 1.7 5.2 5z" fill="#444"/></svg>Login</a>
    </nav>
  </header>

  <main>
    <div class="hero-scene" role="img" aria-label="Photo of hands holding a tablet showing a city map, in front of a blurred city skyline"></div>

    <div class="finder-marker"></div>
    <form class="finder">
      <div class="finder-inner">
        <h1 class="finder-title">Who Would You Like To Find?</h1>
        <input class="finder-input" type="text" placeholder="Find !Wab...">
      </div>
    </form>
    <button class="finder-button" type="button">Look Up</button>

    <section class="activity">
      <h2 class="activity-title">What is the WABLOR™ Social Positioning Phenomenon?</h2>
      <ul class="activity-list">
        <li class="activity-item">!mirelo updated their current location !mirelo.now <span class="activity-time">43 seconds ago</span></li>
        <li class="activity-item">!kovani updated their current location !kovani.now <span class="activity-time">19 minutes ago</span></li>
      </ul>
    </section>
    <a class="activity-more" href="#" aria-label="More updates">
      <svg width="12" height="8" viewBox="0 0 12 8"><path d="M1.5 1.5 6 6l4.5-4.5" stroke="#fff" stroke-width="2.4" fill="none"/></svg>
    </a>

    <a class="support-tab" href="#">Feedback &amp; Support</a>
  </main>

  <footer class="site-footer">
    <nav class="footer-nav">
      <a href="#">About</a><a href="#">Help</a><a href="#">Contact</a><a href="#">Privacy</a><a href="#">Terms</a><a href="#">Refunds</a><a href="#">Faq</a>
    </nav>
    <p class="powered-by">Powered by Wablor API</p>
  </footer>
</body>
</html>
```